Book cover design for a book named BLOOM

Hello Designers,
The name of the book is BLOOM and it is about unexpected experiences individuals have which are beyond their control. Occurrences they are unable to overcome or get out of themselves without the help of God. After overcoming these situations they know only God could have done this for them, no one else could have. It is an adult Christian book. I would like you to be as creative as you can with the cover, using color, light, graphic designs, shapes, scale, lines etc. (you are the designers, I don't know how to do these things.) I would like to use the image created on a paperback, hardcover or e book. I tried to use an image from Pixmarble just to give you some idea of my thinking but you do not have to use these hands. The hands should look as if they are giving someone the word TESTIMONY not receiving it. Use of the words provided, the light rays, and some type of hands extended should not change, but how you use them is up to you. Use the words, light rays, and hands however you wish as long as they convey someone giving the word TESTIMONY. The word TESTIMONY should be proportional to the hand in size and should appear as if being held in the actual hand it should not be larger than the book name. It is a Christian book of testimonies. Also for your design samples you can use the name Marlene Quiller for the author. Thank you, please feel free to contact me if you have any questions. I am looking for the cover to be an attention grabber and give the reader something to really think about and remember visually when they see this cover. Thank you again.

Target Market(s)

anyone and christians

Requirements
Must have
• Use of the words provided, the light rays, and some type of hands extended should not change.
Nice to have
• be as creative as you can with the cover, using color, light, graphic designs, shapes, scale, lines etc. (you are the designers, I don't know how to do these things.)
Should not have
• It should not have fonts, colors, etc. that convey it is a child's book, fairytale, or fictional etc. It is a book of true stories that actually happened. It should not look exactly like my example, what I provided.

```html
<!DOCTYPE html>
<html lang="en">
<head>
<meta charset="utf-8">
<title>BLOOM — Book Cover</title>
<link rel="stylesheet" href="https://fonts.googleapis.com/css2?family=Bebas+Neue&family=Oswald:wght@700&family=Arimo:wght@400;700&display=swap">
<style>
  :root {
    --page: #ffffff;
    --ink: #161616;
    --red-bright: #d10a12;
    --red-deep: #a8070f;
    --robe-light: #fafafb;
    --robe-shade: #dcdee3;
    --glow: #fff8dc;
    --ray: #fffdf2;
    --skin: #efc9b2;
    --skin-mid: #dcaa90;
    --skin-shade: #c98f76;
  }
  * { margin: 0; padding: 0; box-sizing: border-box; }
  html, body {
    width: 1200px; height: 1200px; overflow: hidden;
    background: var(--page);
  }
  .canvas { position: relative; width: 1200px; height: 1200px; }
  .cover {
    position: absolute; left: 246px; top: 65px;
    width: 720px; height: 1078px; overflow: hidden;
  }
  .cover-photo {
    position: absolute; inset: 0;
    background:
      radial-gradient(ellipse 320px 440px at 50% 62%, var(--glow) 0%, rgba(255,248,220,0.55) 38%, rgba(255,255,255,0) 72%),
      linear-gradient(90deg, var(--robe-shade) 0%, var(--robe-light) 22%, #ffffff 50%, var(--robe-light) 78%, var(--robe-shade) 100%);
  }
  .light-rays { position: absolute; inset: 0; width: 720px; height: 1078px; }
  .open-hands {
    position: absolute; left: 70px; top: 800px; width: 580px; height: 250px;
    border-radius: 48% 48% 50% 50% / 30% 30% 70% 70%;
    background:
      radial-gradient(ellipse 46% 40% at 50% 30%, rgba(255,240,228,0.9) 0%, rgba(255,240,228,0) 100%),
      radial-gradient(ellipse 50% 60% at 50% 45%, var(--skin) 0%, var(--skin-mid) 55%, rgba(201,143,118,0.55) 80%, rgba(201,143,118,0) 100%);
    filter: blur(6px);
  }
  .title {
    position: absolute; left: 0; right: 0; top: 64px;
    text-align: center;
    font-family: "Bebas Neue", "Oswald", sans-serif;
    font-weight: 400;
    font-size: 314px; line-height: 1;
    letter-spacing: 2px;
    color: var(--ink);
    transform: scaleX(0.86);
    transform-origin: 50% 0;
  }
  .tagline {
    position: absolute; left: 0; right: 0; top: 354px;
    text-align: center;
    font-family: "Arimo", Arial, sans-serif;
    font-weight: 400;
    font-size: 36px; line-height: 43.5px;
    color: var(--ink);
    text-transform: uppercase;
  }
  .tagline strong { font-weight: 700; }
  .promise {
    position: absolute; left: 0; right: 0; top: 675px;
    text-align: center;
    font-family: "Arimo", Arial, sans-serif;
    font-weight: 700;
    font-size: 35px; line-height: 38px;
    letter-spacing: -0.3px;
    color: var(--red-bright);
  }
  .held-word {
    position: absolute; left: 0; right: 0; top: 762px;
    text-align: center;
    font-family: "Oswald", "Bebas Neue", sans-serif;
    font-weight: 700;
    font-size: 113px; line-height: 1;
    letter-spacing: 1px;
    color: var(--red-deep);
  }
  .author {
    position: absolute; left: 0; right: 0; bottom: 26px;
    text-align: center;
    font-family: "Arimo", Arial, sans-serif;
    font-weight: 700;
    font-size: 24px; line-height: 1;
    letter-spacing: 6px;
    color: var(--ink);
    text-transform: uppercase;
  }
</style>
</head>
<body>
<div class="canvas">
  <div class="cover">
    <div class="cover-photo" role="img" aria-label="Figure in a white robe holding out open cupped hands, offering light that rises in rays from the palms">
      <svg class="light-rays" viewBox="0 0 720 1078" aria-hidden="true">
        <defs>
          <linearGradient id="ray-fade" x1="0" y1="1" x2="0" y2="0">
            <stop offset="0" stop-color="#fffdf2" stop-opacity="0.95"/>
            <stop offset="0.55" stop-color="#fff6d6" stop-opacity="0.45"/>
            <stop offset="1" stop-color="#ffffff" stop-opacity="0"/>
          </linearGradient>
        </defs>
        <g fill="url(#ray-fade)">
          <polygon points="360,860 150,380 200,380"/>
          <polygon points="360,860 230,330 268,330"/>
          <polygon points="360,860 300,300 330,300"/>
          <polygon points="360,860 350,280 372,280"/>
          <polygon points="360,860 392,300 422,300"/>
          <polygon points="360,860 452,330 490,330"/>
          <polygon points="360,860 520,380 570,380"/>
          <polygon points="360,860 80,470 120,450"/>
          <polygon points="360,860 600,450 640,470"/>
        </g>
      </svg>
      <div class="open-hands"></div>
    </div>
    <h1 class="title">BLOOM</h1>
    <p class="tagline">
      Before there will ever be<br>
      a <strong>testimony</strong><br>
      there must always be<br>
      an <strong>experience</strong>
    </p>
    <p class="promise">OUT OF THIS TEST I’VE<br>GIVEN YOU A</p>
    <p class="held-word">TESTIMONY</p>
    <p class="author">Marlene Quiller</p>
  </div>
</div>
</body>
</html>
```